Consulting Company PowerPoint Template Design

We are looking for an updated PowerPoint template design or our 55 person energy consulting firm (K7) based in San Francisco (www.kayseven.example). We would like two versions of the same PowerPoint template in a 16:9 and 4:3 format with our existing logo.

We have an existing color scheme and template and are seeking your help to polish/update the template design for wide format and create a flexible template that is easy to use with content from Excel and Word. Our current template, and a couple of examples that we like are attached.

Specific requests include:

• Dark background for slide title
• A narrow section header
• Maximizing white space for content
• A limited number of well designed Master template layouts to choose from
• A selection of title and section header slides that are not San Francisco specific with some variety to chose from ideally with a focus on energy or nature, graphics/visuals.

For examples of energy specific templates see:
https://www.brightslidery.example/energy/powerpoint-templates/0.html

Requirements
Must have
• Must use our logo but open to other designs, fonts, and styles for the PowerPoint template.
• Please use our existing color scheme found in the attached Excel file.
• Also we would like the ability to easily copy and paste from our existing/original template to the new template. In other words we would like backward compatibility to apply the new template format to our old PowerPoints that use our existing template.

```html
<!DOCTYPE html>
<html lang="en">
<head>
<meta charset="utf-8">
<title>Kayseven Energy Advisors – Presentation Template Set</title>
<link href="https://fonts.googleapis.com/css2?family=Montserrat:wght@400;600;700&family=Open+Sans:wght@400;600;700&display=swap" rel="stylesheet">
<style>
  :root{
    --navy:#0f4e6e;
    --navy-deep:#0b3d57;
    --teal:#1a7fa3;
    --gold:#c8a56a;
    --ink:#1b1b1b;
    --grey-text:#555;
    --slate:#3f4449;
    --stage:#ebe7e1;
    --paper:#ffffff;
    --mist:#dcdcdc;
  }
  *{box-sizing:border-box;margin:0;padding:0}
  html,body{width:1200px;height:1114px;overflow:hidden;background:var(--stage)}
  body{position:relative;font-family:"Open Sans",Arial,sans-serif;color:var(--ink)}
  .slide{position:absolute;width:556px;height:312px;overflow:hidden;
    background:radial-gradient(ellipse at 50% 35%,#ffffff 0%,#f1f1f1 55%,#d6d6d6 100%);
    box-shadow:0 6px 14px rgba(0,0,0,.22)}
  .slide svg.shapes{position:absolute;left:0;top:0;width:556px;height:312px}
  .col-a{left:34px}.col-b{left:610px}
  .row-1{top:54px}.row-2{top:401px}.row-3{top:748px}
  .abs{position:absolute}
  .brand{position:absolute;display:flex;align-items:center;gap:6px}
  .brand-dot{border-radius:50%;background:var(--navy);flex:none}
  .brand-name{font-family:"Open Sans",Arial,sans-serif;font-weight:600;color:var(--navy);white-space:nowrap}
  .cover-title{font-family:"Montserrat",Arial,sans-serif;line-height:1.25}
  .cover-meta{font-size:11px;color:var(--ink)}
  .lead{font-size:7px;line-height:1.35;color:#333}
  /* content slide header */
  .slide-title{position:absolute;left:83px;top:27px;font-family:"Montserrat",Arial,sans-serif;font-weight:700;font-size:20px;color:var(--ink);letter-spacing:.2px}
  .slide-subtitle{position:absolute;left:88px;top:53px;font-family:"Montserrat",Arial,sans-serif;font-weight:700;font-size:16px;color:var(--gold)}
  .corner-mark{position:absolute;right:20px;top:40px;display:flex;align-items:center;gap:4px}
  .corner-mark .brand-dot{width:34px;height:34px}
  .footer-url{position:absolute;left:24px;bottom:2px;font-size:9px;font-weight:700;color:#fff;letter-spacing:.3px}
  .page-no{position:absolute;right:18px;bottom:1px;font-size:10px;font-weight:700;color:var(--ink)}
  /* numbered list */
  .point{position:absolute;display:flex;gap:8px;align-items:flex-start;width:200px}
  .point-num{width:18px;height:18px;background:var(--navy);color:#fff;font-size:11px;font-weight:700;display:flex;align-items:center;justify-content:center;flex:none}
  .point-text{font-size:8.5px;line-height:1.3;color:#444}
  /* timeline */
  .intro{position:absolute;left:30px;top:86px;width:500px;font-size:8px;line-height:1.35;color:#333}
  .milestone{position:absolute;width:110px;text-align:center;transform:translateX(-50%)}
  .milestone h4{font-family:"Montserrat",Arial,sans-serif;font-size:8px;font-weight:700;letter-spacing:.6px;color:var(--ink)}
  .milestone p{font-size:7px;line-height:1.3;color:#555;margin-top:2px}
  .year{font-family:"Montserrat",Arial,sans-serif;font-weight:700;font-size:12px}
  /* team */
  .member{position:absolute;width:100px;text-align:center;transform:translateX(-50%);top:198px}
  .member .name{font-family:"Montserrat",Arial,sans-serif;font-size:10px;font-weight:700;color:var(--gold)}
  .member .role{font-size:7px;color:#444;margin-top:1px}
  .member .bio{font-size:7px;line-height:1.3;color:#444;margin-top:3px;padding:0 6px}
</style>
</head>
<body>

<!-- Cover A: diagonal photo -->
<section class="slide col-a row-1">
  <svg class="shapes" viewBox="0 0 556 312" aria-hidden="false">
    <defs>
      <linearGradient id="leafA" x1="0" y1="0" x2="1" y2="1">
        <stop offset="0" stop-color="#a9d46e"/><stop offset=".5" stop-color="#6fb43e"/><stop offset="1" stop-color="#d8e9b8"/>
      </linearGradient>
    </defs>
    <rect width="556" height="312" fill="#f3f3f3"/>
    <polygon points="0,0 238,0 372,312 0,312" fill="url(#leafA)" role="img" aria-label="Photo: cupped hands sheltering a house outline with an energy-efficiency rating, green foliage background"/>
    <polygon points="238,0 258,0 392,312 372,312" fill="var(--navy)"/>
    <polygon points="262,0 267,0 401,312 396,312" fill="var(--gold)"/>
  </svg>
  <div class="brand" style="left:302px;top:46px">
    <span class="brand-dot" style="width:40px;height:40px"></span>
    <span class="brand-name" style="font-size:11px">Kayseven Energy Advisors</span>
  </div>
  <div class="cover-title abs" style="right:14px;top:110px;text-align:right;font-weight:700;font-size:24px">PRESENTATION<br>TEMPLETE</div>
  <p class="lead abs" style="right:14px;top:186px;width:188px;text-align:right">Lorem Ipsum is simply dummy text of the printing and typesetting industry. Lorem Ipsum has been the industry's standard dummy text ever since the 1500s, when an unknown printer took a galley of type and scrambled it to make a type specimen book. It has survived not only five centuries, but also the leap into electronic typesetting.</p>
</section>

<!-- Cover B: curved photo right -->
<section class="slide col-b row-1" style="background:#fff">
  <svg class="shapes" viewBox="0 0 556 312">
    <defs>
      <linearGradient id="leafB" x1="0" y1="0" x2="1" y2="1">
        <stop offset="0" stop-color="#cfe6a6"/><stop offset=".5" stop-color="#79b947"/><stop offset="1" stop-color="#a7d073"/>
      </linearGradient>
    </defs>
    <path d="M335,0 C300,110 270,220 190,312 L556,312 L556,0 Z" fill="url(#leafB)" role="img" aria-label="Photo: cupped hands sheltering a house outline with an energy-efficiency rating, green foliage background"/>
    <path d="M312,0 L335,0 C300,110 270,220 190,312 L0,312 L0,282 L190,282 C245,210 285,110 312,0 Z" fill="var(--navy)"/>
    <path d="M304,0 L310,0 C283,110 243,212 186,278 L0,278 L0,274 L182,274 C238,208 278,110 304,0 Z" fill="var(--gold)"/>
  </svg>
  <div class="brand" style="left:26px;top:56px">
    <span class="brand-dot" style="width:46px;height:46px"></span>
    <span class="brand-name" style="font-size:12px">Kayseven Energy Advisors</span>
  </div>
  <div class="cover-title abs" style="left:30px;top:142px;font-weight:400;font-size:24px">PRESENTATION<br>TEMPLETE</div>
  <div class="cover-meta abs" style="left:30px;top:216px;line-height:1.5">Client name: Daniel Morrow<br>Date: 25/5/2018</div>
</section>

<!-- Cover C: wave band -->
<section class="slide col-a row-2">
  <svg class="shapes" viewBox="0 0 556 312">
    <path d="M0,150 Q278,88 556,112 L556,312 L0,312 Z" fill="var(--navy)"/>
    <path d="M0,138 Q278,74 556,98 L556,108 Q278,84 0,146 Z" fill="var(--gold)"/>
    <path d="M0,146 Q278,84 556,108 L556,112 Q278,88 0,150 Z" fill="#fff"/>
  </svg>
  <div class="brand" style="left:44px;top:56px">
    <span class="brand-dot" style="width:60px;height:60px"></span>
    <span class="brand-name" style="font-size:16px">Kayseven Energy Advisors</span>
  </div>
  <div class="cover-title abs" style="right:34px;top:186px;text-align:right;color:#fff;font-weight:400;font-size:26px">PRESENTATION<br>TEMPLETE</div>
  <div class="cover-meta abs" style="right:34px;top:268px;color:#fff;font-size:10.5px">Client name: Daniel Morrow &nbsp;|&nbsp; Date: 25/5/2018</div>
</section>

<!-- Content: numbered list -->
<section class="slide col-b row-2">
  <svg class="shapes" viewBox="0 0 556 312">
    <polygon points="0,26 64,26 76,48 0,48" fill="var(--teal)"/>
    <polygon points="20,26 64,26 76,48 32,48" fill="var(--navy)"/>
    <line x1="248" y1="64" x2="500" y2="64" stroke="#bdbdbd" stroke-width="1"/>
    <rect x="0" y="296" width="556" height="16" fill="var(--navy)"/>
    <polygon points="500,296 556,296 556,312 492,312" fill="var(--gold)"/>
  </svg>
  <h2 class="slide-title">TITLE FOR THE SLIDE</h2>
  <p class="slide-subtitle">Subtitle Goes here</p>
  <div class="corner-mark"><span class="brand-dot"></span></div>
  <div class="point" style="left:86px;top:104px"><span class="point-num">1</span><span class="point-text">Lorem Ipsum is simply dummy text of the printing and typesetting industry.</span></div>
  <div class="point" style="left:86px;top:148px"><span class="point-num">2</span><span class="point-text">Lorem Ipsum is simply dummy text of the printing and typesetting industry.</span></div>
  <div class="point" style="left:86px;top:192px"><span class="point-num">3</span><span class="point-text">Lorem Ipsum is simply dummy text of the printing and typesetting industry.</span></div>
  <div class="point" style="left:86px;top:236px"><span class="point-num">4</span><span class="point-text">Lorem Ipsum is simply dummy text of the printing and typesetting industry.</span></div>
  <div class="point" style="left:306px;top:104px"><span class="point-num">5</span><span class="point-text">Lorem Ipsum is simply dummy text of the printing and typesetting industry.</span></div>
  <div class="point" style="left:306px;top:148px"><span class="point-num">6</span><span class="point-text">Lorem Ipsum is simply dummy text of the printing and typesetting industry.</span></div>
  <div class="point" style="left:306px;top:192px"><span class="point-num">7</span><span class="point-text">Lorem Ipsum is simply dummy text of the printing and typesetting industry.</span></div>
  <div class="point" style="left:306px;top:236px"><span class="point-num">8</span><span class="point-text">Lorem Ipsum is simply dummy text of the printing and typesetting industry.</span></div>
  <span class="footer-url">www.kayseven.example</span>
  <span class="page-no">1</span>
</section>

<!-- Content: timeline -->
<section class="slide col-a row-3">
  <svg class="shapes" viewBox="0 0 556 312">
    <polygon points="0,26 64,26 76,48 0,48" fill="var(--teal)"/>
    <polygon points="20,26 64,26 76,48 32,48" fill="var(--navy)"/>
    <line x1="248" y1="64" x2="500" y2="64" stroke="#bdbdbd" stroke-width="1"/>
    <path d="M70,198 C100,196 118,176 142,177 S192,212 216,212 S264,181 288,181 S338,216 362,216 S410,181 433,181 S500,200 540,186" fill="none" stroke="var(--gold)" stroke-width="2"/>
    <path d="M433,181 S500,200 540,186" fill="none" stroke="var(--navy)" stroke-width="2"/>
    <g stroke="#9a9a9a" stroke-width="1">
      <line x1="216" y1="140" x2="216" y2="188"/><line x1="356" y1="140" x2="362" y2="192"/>
      <line x1="142" y1="201" x2="142" y2="244"/><line x1="288" y1="205" x2="288" y2="244"/><line x1="433" y1="205" x2="433" y2="244"/>
    </g>
    <g>
      <circle cx="142" cy="177" r="24" fill="var(--gold)"/><circle cx="142" cy="177" r="18" fill="#fff"/>
      <circle cx="216" cy="212" r="24" fill="var(--slate)"/><circle cx="216" cy="212" r="18" fill="#fff"/>
      <circle cx="288" cy="181" r="24" fill="var(--navy)"/><circle cx="288" cy="181" r="18" fill="#fff"/>
      <circle cx="362" cy="216" r="24" fill="var(--gold)"/><circle cx="362" cy="216" r="18" fill="#fff"/>
      <circle cx="433" cy="181" r="24" fill="var(--navy)"/><circle cx="433" cy="181" r="18" fill="#fff"/>
    </g>
    <g font-family="Montserrat, Arial, sans-serif" font-weight="700" font-size="12" text-anchor="middle">
      <text x="142" y="181" fill="var(--gold)">2006</text>
      <text x="216" y="216" fill="var(--slate)">2010</text>
      <text x="288" y="185" fill="var(--navy)">2012</text>
      <text x="362" y="220" fill="var(--gold)">2015</text>
      <text x="433" y="185" fill="var(--navy)">2018</text>
    </g>
    <rect x="0" y="296" width="556" height="16" fill="var(--navy)"/>
    <polygon points="500,296 556,296 556,312 492,312" fill="var(--gold)"/>
  </svg>
  <h2 class="slide-title">TITLE FOR THE SLIDE</h2>
  <p class="slide-subtitle">Subtitle Goes here</p>
  <div class="corner-mark"><span class="brand-dot"></span></div>
  <p class="intro">Lorem ipsum dolor sit amet, consectetur adipiscing elit, sed do eiusmod tempor incididunt ut labore et dolore magna aliqua. Ut enim ad minim veniam, quis nostrud exercitation ullamco laboris nisi ut aliquip ex ea commodo.</p>
  <div class="milestone" style="left:216px;top:110px"><h4>LOREM IPSUM</h4><p>Lorem Ipsum is simply dummy text of the printing and typesetting industry.</p></div>
  <div class="milestone" style="left:356px;top:110px"><h4>LOREM IPSUM</h4><p>Lorem Ipsum is simply dummy text of the printing and typesetting industry.</p></div>
  <div class="milestone" style="left:142px;top:246px"><h4>LOREM IPSUM</h4><p>Lorem Ipsum is simply dummy text of the printing and typesetting industry.</p></div>
  <div class="milestone" style="left:288px;top:246px"><h4>LOREM IPSUM</h4><p>Lorem Ipsum is simply dummy text of the printing and typesetting industry.</p></div>
  <div class="milestone" style="left:433px;top:246px"><h4>LOREM IPSUM</h4><p>Lorem Ipsum is simply dummy text of the printing and typesetting industry.</p></div>
  <span class="footer-url">www.kayseven.example</span>
  <span class="page-no">1</span>
</section>

<!-- Content: team -->
<section class="slide col-b row-3">
  <svg class="shapes" viewBox="0 0 556 312">
    <defs>
      <radialGradient id="portrait" cx=".5" cy=".4" r=".6">
        <stop offset="0" stop-color="#e9e6e2"/><stop offset="1" stop-color="#b9b4ae"/>
      </radialGradient>
    </defs>
    <polygon points="0,26 64,26 76,48 0,48" fill="var(--teal)"/>
    <polygon points="20,26 64,26 76,48 32,48" fill="var(--navy)"/>
    <line x1="248" y1="64" x2="500" y2="64" stroke="#bdbdbd" stroke-width="1"/>
    <g stroke="#fff" stroke-width="3">
      <circle cx="78" cy="145" r="44" fill="url(#portrait)" role="img" aria-label="Team member portrait photo"/>
      <circle cx="182" cy="145" r="44" fill="url(#portrait)" role="img" aria-label="Team member portrait photo"/>
      <circle cx="288" cy="145" r="44" fill="url(#portrait)" role="img" aria-label="Team member portrait photo"/>
      <circle cx="393" cy="145" r="44" fill="url(#portrait)" role="img" aria-label="Team member portrait photo"/>
      <circle cx="490" cy="145" r="44" fill="url(#portrait)" role="img" aria-label="Team member portrait photo"/>
    </g>
    <rect x="0" y="296" width="556" height="16" fill="var(--navy)"/>
    <polygon points="500,296 556,296 556,312 492,312" fill="var(--gold)"/>
  </svg>
  <h2 class="slide-title">TITLE FOR THE SLIDE</h2>
  <p class="slide-subtitle">Subtitle Goes here</p>
  <div class="corner-mark"><span class="brand-dot"></span></div>
  <div class="member" style="left:78px"><p class="name">Daniel Morrow</p><p class="role">Manager</p><p class="bio">Lorem Ipsum is simply dummy text of the printing and typesetting industry. Lorem Ipsum has been the industry's standard</p></div>
  <div class="member" style="left:182px"><p class="name">Daniel Morrow</p><p class="role">Manager</p><p class="bio">Lorem Ipsum is simply dummy text of the printing and typesetting industry. Lorem Ipsum has been the industry's standard</p></div>
  <div class="member" style="left:288px"><p class="name">Daniel Morrow</p><p class="role">Manager</p><p class="bio">Lorem Ipsum is simply dummy text of the printing and typesetting industry. Lorem Ipsum has been the industry's standard</p></div>
  <div class="member" style="left:393px"><p class="name">Daniel Morrow</p><p class="role">Manager</p><p class="bio">Lorem Ipsum is simply dummy text of the printing and typesetting industry. Lorem Ipsum has been the industry's standard</p></div>
  <div class="member" style="left:490px"><p class="name">Daniel Morrow</p><p class="role">Manager</p><p class="bio">Lorem Ipsum is simply dummy text of the printing and typesetting industry. Lorem Ipsum has been the industry's standard</p></div>
  <span class="footer-url">www.kayseven.example</span>
  <span class="page-no">1</span>
</section>

</body>
</html>
```